Plum & Us Business Card Design

Plum & Us is a company that makes treats and real food for people with food allergies, illnesses and those that like to eat clean. We like to take good old fashioned favorites and create a clean, healthy version of it without losing any of the addictive ‘yumminess’ of it.All of our products are made with Organic ingredients and we aim to be as sustainable as possible therefore I would like this to be reflected in our business cards. I like the thought of using chia seeds in the business card maybe so that people could grow their own.

Industry/Entity Type

Health And Wellness

Contact Information for Business Card

Plum & Uswww.plumandus.com.aumarnie@plumandus.com.auP: 0431 596 218 Facebook and Instagram logos

Requirements
Must have
• Logo - does not have to be the exact logo as long as it is close and fits in with the other information I have asked for (sustainable & Organic, recycled etc.)
• See the photo with the treats for a picture of the logo

```html
<!DOCTYPE html>
<html lang="en">
<head>
<meta charset="utf-8">
<title>Plum &amp; Us — Business Card</title>
<link rel="stylesheet" href="https://fonts.googleapis.com/css2?family=Open+Sans:wght@300;400;700&display=swap">
<style>
  :root {
    --page-bg: #e9e6e1;
    --card-deep: #2a2474;
    --card-mid: #3a3392;
    --card-light: #4a44a6;
    --ink: #ffffff;
    --ink-soft: rgba(255,255,255,0.82);
    --decor: rgba(255,255,255,0.10);
  }
  * { box-sizing: border-box; margin: 0; padding: 0; }
  html, body {
    width: 1200px; height: 1022px; overflow: hidden;
    background: var(--page-bg);
    font-family: "Open Sans", Arial, sans-serif;
  }
  .stage {
    width: 1200px; height: 1022px;
    display: flex; align-items: center; justify-content: center;
  }
  .card {
    position: relative;
    width: 900px; height: 514px;
    border-radius: 18px;
    overflow: hidden;
    background: linear-gradient(135deg, var(--card-deep) 0%, var(--card-mid) 55%, var(--card-light) 100%);
    box-shadow: 0 18px 40px rgba(30, 24, 70, 0.28);
    color: var(--ink);
  }
  .leaf-decor {
    position: absolute;
    left: 470px; top: 250px;
    width: 250px; height: 250px;
    border-radius: 50%;
    background: radial-gradient(circle, var(--decor) 0%, rgba(255,255,255,0.04) 70%, transparent 72%);
  }
  .brand {
    position: absolute;
    left: 60px; bottom: 64px;
    font-size: 58px;
    font-weight: 300;
    letter-spacing: 1px;
    line-height: 1.2;
    color: var(--ink);
    white-space: nowrap;
  }
  .contact {
    position: absolute;
    right: 56px; top: 52px;
    text-align: right;
  }
  .contact__name {
    font-size: 34px; font-weight: 700; letter-spacing: 1px;
    text-transform: uppercase; line-height: 1.1;
  }
  .contact__role {
    font-size: 19px; font-weight: 300; letter-spacing: 1.5px;
    text-transform: uppercase; margin-top: 4px;
  }
  .contact__list { list-style: none; margin-top: 22px; }
  .contact__item {
    display: flex; justify-content: flex-end; align-items: center; gap: 12px;
    font-size: 19px; font-weight: 300; color: var(--ink-soft);
    line-height: 1.75; white-space: nowrap;
  }
  .contact__icon { width: 16px; height: 16px; flex: none; }
  .social {
    position: absolute;
    right: 56px; bottom: 48px;
    display: flex; gap: 14px;
  }
  .social__mark {
    width: 24px; height: 24px; border-radius: 5px;
    background: var(--ink);
  }
</style>
</head>
<body>
<main class="stage">
  <section class="card" aria-label="Plum &amp; Us business card">
    <div class="leaf-decor" role="img" aria-label="Faint leaf emblem decoration"></div>

    <div class="brand">Plum &amp; Us</div>

    <div class="contact">
      <h1 class="contact__name">Rowan Tate</h1>
      <p class="contact__role">Director</p>
      <ul class="contact__list">
        <li class="contact__item">0431 596 218
          <svg class="contact__icon" viewBox="0 0 16 16" aria-hidden="true"><path d="M4 1.5c.6 0 1.6 2.6 1.6 3.2 0 .7-1.2 1-1.2 1.7 0 1 2.3 3.9 3.4 4.3.6.2 1-1 1.7-1 .6 0 3 1.3 3 1.9 0 1.3-1.6 2.9-3 2.9C6 14.5 1.5 9 1.5 5 1.5 3.4 2.8 1.5 4 1.5z" fill="#fff"/></svg>
        </li>
        <li class="contact__item">marnie@plumandus.com.au
          <svg class="contact__icon" viewBox="0 0 16 16" aria-hidden="true"><rect x="1" y="3" width="14" height="10" rx="1.5" fill="none" stroke="#fff" stroke-width="1.5"/><path d="M1.5 4l6.5 5 6.5-5" fill="none" stroke="#fff" stroke-width="1.5"/></svg>
        </li>
        <li class="contact__item">www.plumandus.com.au
          <svg class="contact__icon" viewBox="0 0 16 16" aria-hidden="true"><circle cx="8" cy="8" r="6.5" fill="none" stroke="#fff" stroke-width="1.4"/><ellipse cx="8" cy="8" rx="2.8" ry="6.5" fill="none" stroke="#fff" stroke-width="1.2"/><path d="M1.5 8h13" stroke="#fff" stroke-width="1.2"/></svg>
        </li>
      </ul>
    </div>

    <div class="social" role="group" aria-label="Social profiles">
      <span class="social__mark" role="img" aria-label="Social profile one"></span>
      <span class="social__mark" role="img" aria-label="Social profile two"></span>
    </div>
  </section>
</main>
</body>
</html>
```